Business Cards & Stationary for Law Firm using great new logo!
BrisvaleMoor LLC
Simple
Corinne T.Wexby, Esq.
712 Pruett Avenue
Wilmington, DE 19801
corinne.wexby@brisvalemoor-example.com
brisvalemoor-example.com
The front of the card should have the attorney name & email, the Firm name, address, phone, fax and website.
If the font used in the logo allows for lower case letters, please use the same font. BUT, if the font used in the logo requires all capitals (small caps and large caps), then please use standard fonts instead.
The logo design should be on the back of the card.
This is a higher resolution version of the logo. Please use this file going forward.

```html
<!DOCTYPE html>
<html lang="en">
<head>
<meta charset="utf-8">
<title>BrisvaleMoor LLC – Business Card</title>
<link rel="stylesheet" href="https://fonts.googleapis.com/css2?family=Cormorant+Garamond:wght@500;600;700&display=swap">
<style>
  :root {
    --backdrop: #2e2e30;
    --card: #ffffff;
    --card-shade: #f1f1f3;
    --navy: #1d2a8f;
    --navy-deep: #121b66;
    --ink: #4a4a52;
    --rule: #b9bbc8;
  }
  * { box-sizing: border-box; margin: 0; padding: 0; }
  html, body {
    width: 1200px; height: 901px; overflow: hidden;
    background: var(--backdrop);
    font-family: "Cormorant Garamond", "Times New Roman", serif;
  }
  .card {
    position: absolute;
    left: 240px;
    width: 720px; height: 410px;
    background: linear-gradient(180deg, var(--card) 0%, var(--card) 70%, var(--card-shade) 100%);
    box-shadow: 0 10px 30px rgba(0,0,0,.45);
  }
  .card--back { top: 26px; }
  .card--front { top: 465px; }

  /* back */
  .back-brand {
    position: absolute; inset: 0;
    display: flex; align-items: center; justify-content: center; gap: 18px;
  }
  .brand-square { width: 46px; height: 46px; background: var(--navy); }
  .brand-name {
    font-size: 46px; font-weight: 700; color: var(--navy); letter-spacing: .5px;
  }
  .back-web {
    position: absolute; right: 40px; top: 262px;
    font-size: 15px; color: var(--ink); letter-spacing: 1px;
  }

  /* front */
  .front-brand {
    position: absolute; left: 250px; top: 52px;
    display: flex; align-items: center; gap: 12px;
  }
  .front-brand .brand-square { width: 30px; height: 30px; }
  .front-brand .brand-name { font-size: 36px; }

  .attorney {
    position: absolute; left: 300px; top: 150px; width: 300px;
    text-align: center;
    font-size: 21px; font-weight: 600; color: var(--navy);
    border-bottom: 1px solid var(--rule); padding-bottom: 4px;
  }
  .attorney span { font-weight: 500; }

  .contact {
    position: absolute; right: 306px; top: 188px;
    text-align: right; font-size: 15px; line-height: 19px; color: var(--ink);
  }
  .divider {
    position: absolute; left: 426px; top: 190px; width: 1px; height: 58px;
    background: var(--rule);
  }
  .address {
    position: absolute; left: 440px; top: 188px;
    font-size: 15px; line-height: 19px; color: var(--ink);
  }

  .band-rule {
    position: absolute; left: 0; right: 0; height: 2px; background: var(--navy);
  }
  .band-rule--top { top: 318px; }
  .band {
    position: absolute; left: 0; right: 0; top: 326px; height: 28px;
    background: linear-gradient(90deg, var(--navy-deep) 0%, var(--navy) 55%, #5d6bd0 85%, #c9cdf0 100%);
    display: flex; align-items: center; padding-left: 40px;
  }
  .band-web { color: #fff; font-size: 14px; letter-spacing: 3px; }
  .band-rule--bottom { top: 362px; height: 1px; background: #7b84c8; }
</style>
</head>
<body>

<section class="card card--back" aria-label="Card back">
  <div class="back-brand">
    <div class="brand-square"></div>
    <div class="brand-name">BrisvaleMoor LLC</div>
  </div>
</section>

<section class="card card--front" aria-label="Card front">
  <div class="front-brand">
    <div class="brand-square"></div>
    <div class="brand-name">BrisvaleMoor LLC</div>
  </div>

  <p class="attorney">Corinne T.Wexby<span>, Esq.</span></p>

  <div class="contact">
    <p>P. 302.555.0146</p>
    <p>F. 302.555.0147</p>
    <p>E. corinne.wexby@brisvalemoor-example.com</p>
  </div>
  <div class="divider"></div>
  <div class="address">
    <p>BrisvaleMoor LLC</p>
    <p>712 Pruett Avenue</p>
    <p>Wilmington, DE 19801</p>
  </div>

  <div class="band-rule band-rule--top"></div>
  <div class="band"><span class="band-web">www.brisvalemoor-example.com</span></div>
  <div class="band-rule band-rule--bottom"></div>
</section>

</body>
</html>
```